Market Research firm needs updated business cards with new logo

We need the logo to be included somewhere on the card (attached). We would also like the phrases "Independent, Objective, Comprehensive" and "Research You Can Trust" somewhere on the card. Front or back. Our colors are hex codes 6075a7, e48d25 and 5a5b5b. Though you are certainly not limited to those shades, whatever you produce should coordinate with them. I have also attached our favicon. Feel free to use it in your design, but please do not use it to replace the full logo.

Contact Information for Business Card

see project description

Other font styles liked:
• Open Sans

Requirements
Must have
• the logo
• We use Open Sans font

```html
<!DOCTYPE html>
<html lang="en">
<head>
<meta charset="utf-8">
<title>Orvane Research – Business Card</title>
<link rel="stylesheet" href="https://fonts.googleapis.com/css2?family=Arimo:wght@400;600;700&display=swap">
<style>
  :root {
    --stage: #000000;
    --slate: #5a5b5b;
    --paper: #e6e6e6;
    --orange: #e48d25;
    --blue: #6075a7;
  }
  * { margin: 0; padding: 0; box-sizing: border-box; }
  html, body { width: 1200px; height: 1200px; overflow: hidden; background: var(--stage); }
  body { position: relative; font-family: "Arimo", Arial, sans-serif; }

  .card { position: absolute; left: 180px; width: 840px; height: 480px; overflow: hidden; }
  .card--front { top: 97px; }
  .card--back { top: 622px; }

  .band { position: absolute; left: 0; width: 100%; }
  .band--slate { background: var(--slate); }
  .band--paper { background: var(--paper); }
  .band--blue { background: var(--blue); }

  .wordmark { position: absolute; display: flex; align-items: center; color: var(--orange); font-weight: 600; white-space: nowrap; }
  .wordmark__dot { border-radius: 50%; background: var(--orange); flex: none; }

  .front-head { top: 0; height: 139px; }
  .front-head .wordmark { left: 60px; top: 42px; font-size: 38px; gap: 12px; }
  .front-head .wordmark__dot { width: 22px; height: 22px; }

  .front-body { top: 139px; height: 297px; }
  .person { position: absolute; left: 126px; top: 18px; color: var(--orange); }
  .person__name { font-size: 37px; font-weight: 700; letter-spacing: 0.5px; line-height: 1; }
  .person__role { font-size: 25px; font-weight: 400; margin-left: 6px; line-height: 1; }

  .contacts { position: absolute; left: 64px; top: 110px; list-style: none; }
  .contacts li { display: flex; align-items: center; height: 28px; margin-bottom: 25px; }
  .contacts li:nth-child(3) { margin-top: -4px; }
  .contacts svg { width: 32px; height: 28px; flex: none; }
  .contacts span { margin-left: 30px; color: var(--orange); font-size: 23px; }

  .accent-ring { position: absolute; left: 544px; top: 39px; width: 216px; height: 216px; border-radius: 50%; border: 18px solid var(--orange); }

  .front-foot { top: 436px; height: 44px; }
  .tagline { position: absolute; top: 13px; color: var(--orange); font-size: 19px; font-weight: 700; letter-spacing: 0.3px; white-space: nowrap; }
  .tagline--a { left: 46px; }
  .tagline--b { left: 258px; }
  .tagline--c { left: 498px; top: 15px; }

  .back-top { top: 0; height: 148px; }
  .back-mid { top: 148px; height: 186px; }
  .back-bot { top: 334px; height: 146px; }
  .back-mid .wordmark { left: 60px; top: 46px; font-size: 84px; gap: 20px; letter-spacing: -1px; }
  .back-mid .wordmark__dot { width: 44px; height: 44px; }
</style>
</head>
<body>

<section class="card card--front" aria-label="Business card front">
  <div class="band band--slate front-head">
    <div class="wordmark"><span class="wordmark__dot"></span>Orvane Research</div>
  </div>

  <div class="band band--paper front-body">
    <div class="person">
      <div class="person__name">DANA WHITFIELD</div>
      <div class="person__role">Owner</div>
    </div>

    <ul class="contacts">
      <li>
        <svg viewBox="0 0 32 28" aria-hidden="true"><rect x="1.5" y="4" width="29" height="21" fill="none" stroke="#6075a7" stroke-width="2.5"/><path d="M2 5 L16 17 L30 5 M2 24 L12 14 M30 24 L20 14" fill="none" stroke="#6075a7" stroke-width="2.2"/></svg>
        <span>dana@orvanemail.com</span>
      </li>
      <li>
        <svg viewBox="0 0 32 28" aria-hidden="true"><circle cx="14" cy="14" r="13" fill="#6075a7"/><path d="M9 8 l3 -1 2 4 -2 1.5 c1 2 2.5 3.5 4.5 4.5 l1.5 -2 4 2 -1 3 c-6 0 -12 -6 -12 -12z" fill="#e6e6e6"/></svg>
        <span>555 0142 3387</span>
      </li>
      <li>
        <svg viewBox="0 0 32 28" aria-hidden="true"><g fill="none" stroke="#6075a7" stroke-width="2"><circle cx="15" cy="14" r="12.5"/><ellipse cx="15" cy="14" rx="5.5" ry="12.5"/><path d="M2.5 14 H27.5 M5 7.5 H25 M5 20.5 H25"/></g></svg>
        <span>www.orvaneresearch.com</span>
      </li>
    </ul>

    <div class="accent-ring" aria-hidden="true"></div>
  </div>

  <div class="band band--blue front-foot">
    <span class="tagline tagline--a">INDEPENDENT</span>
    <span class="tagline tagline--b">COMPREHENSIVE</span>
    <span class="tagline tagline--c">RESEARCH YOU CAN TRUST</span>
  </div>
</section>

<section class="card card--back" aria-label="Business card back">
  <div class="band band--slate back-top"></div>
  <div class="band band--paper back-mid">
    <div class="wordmark"><span class="wordmark__dot"></span>Orvane Research</div>
  </div>
  <div class="band band--slate back-bot"></div>
</section>

</body>
</html>
```